Veridan Crest Business Cards

Veridan Crest Prestige Portfolio Group is a global representation business focusing on high end luxury. We need business cards to epitomize our global, luxury delivery model.

Target Market(s)

Global Representation in the hospitality industry

Industry/Entity Type

Hospitality

Contact Information for Business Card

name
title
email: first.last@vc-ppg.com
web: www.vc-ppg.com
mobile:

Requirements
Must have
• double sided design
• incorporate logo colours
• have logo prominent
Should not have
• no designs not incorporating logo colours.

```html
<!DOCTYPE html>
<html lang="en">
<head>
<meta charset="utf-8">
<title>Veridan Crest Business Cards</title>
<link rel="stylesheet" href="https://fonts.googleapis.com/css2?family=Libre+Baskerville:wght@400;700&display=swap">
<style>
  :root {
    --stage: #1d1d20;
    --gold: #7f6b3d;
    --gold-light: #93805a;
    --gold-soft: #8a7650;
    --white: #ffffff;
    --serif: "Libre Baskerville", "Times New Roman", serif;
  }
  * { margin: 0; padding: 0; box-sizing: border-box; }
  html, body { width: 1200px; height: 800px; overflow: hidden; }
  body {
    background: var(--stage);
    font-family: var(--serif);
    display: flex;
    flex-direction: column;
    align-items: center;
    justify-content: center;
    gap: 40px;
  }
  .card {
    width: 600px;
    height: 340px;
    border-radius: 22px;
    overflow: hidden;
    position: relative;
    box-shadow: 0 18px 40px rgba(0,0,0,.45);
  }

  /* Front */
  .card--front { background: var(--gold); }
  .front__map {
    position: absolute;
    left: 70px; top: 40px;
    width: 470px; height: 260px;
    border-radius: 60px 90px 70px 110px;
    background: radial-gradient(ellipse at 55% 45%, var(--gold-light) 0%, var(--gold-soft) 55%, var(--gold) 100%);
    opacity: .9;
  }
  .brand {
    position: absolute;
    inset: 0;
    display: flex;
    flex-direction: column;
    align-items: center;
    justify-content: center;
    text-align: center;
  }
  .brand__name {
    font-size: 46px;
    font-weight: 700;
    letter-spacing: 1px;
    line-height: 1.1;
  }
  .brand__tagline {
    margin-top: 14px;
    font-size: 11px;
    letter-spacing: 3px;
    text-transform: uppercase;
  }
  .card--front .brand { color: var(--white); }

  /* Back */
  .card--back { display: flex; background: var(--gold); }
  .back__logo-panel {
    width: 300px;
    height: 100%;
    background: var(--white);
    position: relative;
    color: var(--gold);
  }
  .back__logo-panel .brand__name { font-size: 34px; }
  .back__logo-panel .brand__tagline { font-size: 8.5px; letter-spacing: 2px; }
  .back__contact {
    flex: 1;
    color: var(--white);
    padding: 70px 0 0 34px;
  }
  .contact__name {
    font-size: 17px;
    font-weight: 700;
    letter-spacing: 1px;
    text-transform: uppercase;
  }
  .contact__title { font-size: 11px; margin-top: 2px; }
  .contact__address { font-size: 11px; line-height: 1.6; margin-top: 18px; }
  .contact__list { list-style: none; margin-top: 10px; font-size: 11px; line-height: 1.9; }
  .contact__list li { display: flex; align-items: center; gap: 8px; }
  .contact__list svg { width: 11px; height: 11px; flex: none; }
  .contact__web { letter-spacing: 2px; }
</style>
</head>
<body>

  <section class="card card--front" aria-label="Business card front">
    <div class="front__map" role="img" aria-label="Faint world map in light gold across the card"></div>
    <div class="brand">
      <span class="brand__name">Veridan Crest</span>
      <span class="brand__tagline">Prestige Portfolio Group</span>
    </div>
  </section>

  <section class="card card--back" aria-label="Business card back">
    <div class="back__logo-panel">
      <div class="brand">
        <span class="brand__name">Veridan Crest</span>
        <span class="brand__tagline">Prestige Portfolio Group</span>
      </div>
    </div>
    <div class="back__contact">
      <p class="contact__name">Marcus Hale</p>
      <p class="contact__title">Director</p>
      <p class="contact__address">PO Box 418, Harlow Street<br>7th Lane, Arizona</p>
      <ul class="contact__list">
        <li>
          <svg viewBox="0 0 12 12" aria-hidden="true"><rect x="1.5" y="1.5" width="9" height="9" fill="none" stroke="#fff" stroke-width="1.4"/></svg>
          (555) 010 4821
        </li>
        <li>
          <svg viewBox="0 0 12 12" aria-hidden="true"><rect x="1" y="2.5" width="10" height="7" fill="#fff"/><path d="M1 2.5 L6 7 L11 2.5" fill="none" stroke="#7f6b3d" stroke-width="1"/></svg>
          first.last@vc-ppg.com
        </li>
        <li class="contact__web">
          <svg viewBox="0 0 12 12" aria-hidden="true"><circle cx="6" cy="6" r="5" fill="#fff"/><path d="M1 6 H11 M6 1 V11" stroke="#7f6b3d" stroke-width=".8"/></svg>
          www.vc-ppg.com
        </li>
      </ul>
    </div>
  </section>

</body>
</html>
```